Web Design for Small Healthcare Startup

Hello,

We are seeking a Website Design for a healthcare company focusing on mobile vaccinations, employee health and wellness services onsite at businesses, and consulting services relating to Healthcare Entities in WA state. Our company’s mission is to “To aid in a healthier workplace”. Brightpath Rovers will provide on-site wellness services to employers that simplify and streamline employee preventative health as well as onsite consulting services to help with compliance of Healthcare Entities.

We are seeking a Website Design for Brightpath Rovers, PLLC. Our company’s mission is to provide mobile health and wellness services to employers onsite at their businesses. These services include mobile vaccinations clinics for employees as well as wellness and health screenings. The company will also offer healtcare compliance consulting services for Healthcare Entities. The company was founded to bring these important healthcare services to businesses and keep employees healthy. Healthy employees are the cornerstone to a great business and we want to help orginazations achieve their goals of having a healthy productive workforce.

We are looking for a moderin website design that will need to be coded. We have attached our current logo design for reference as well as a brief questionare regarding our business for your information (not necessary to include all information). We would like something SEO friendly and easy to navigate.

Thank you!

Brightpath Rovers, PLLC

Target Market(s)

Small Businesses

Industry/Entity Type

Healthcare

Coding

Coded - Design and coding required

Number of Pages Required

1 page

Requirements
Nice to have
• SEO Friendly, Incorporate Logo

```html
<!DOCTYPE html>
<html lang="en">
<head>
<meta charset="utf-8">
<title>Brightpath Rovers, PLLC – On-Site Mobile Vaccine Clinics</title>
<link href="https://fonts.googleapis.com/css2?family=Poppins:wght@300;400;500;600;700&display=swap" rel="stylesheet">
<style>
:root{
  --purple:#9c3f98;
  --purple-soft:#efe0ef;
  --blue:#1b4fa0;
  --blue-deep:#16489a;
  --ring:#cdd6ea;
  --text:#5d5d6b;
  --tint:#f8f6fb;
  --tint-blue:#f2f5fb;
  --white:#ffffff;
}
*{box-sizing:border-box;margin:0;padding:0}
html,body{width:1200px;height:3724px;overflow:hidden}
body{font-family:'Poppins',sans-serif;color:var(--text);background:var(--white);position:relative}
.abs{position:absolute}
a{text-decoration:none;color:inherit}
.btn{position:absolute;display:flex;align-items:center;justify-content:center;border-radius:20px;font-size:14px;font-weight:400}
.btn-blue{background:var(--blue);color:var(--white)}
.btn-white{background:var(--white);color:var(--blue)}
.brand{font-weight:600;color:var(--blue);display:flex;align-items:center;gap:8px}
.brand-dot{width:14px;height:14px;border-radius:50%;background:var(--purple)}
.accent{color:var(--purple)}

/* top bar */
.topbar{left:0;top:0;width:1200px;height:38px;background:var(--purple);color:var(--white);font-size:12px}
.topbar .promo{left:61px;top:11px}
.topbar .contact{top:8px;display:flex;align-items:center;gap:8px;font-size:14px}
.ico-circle{width:24px;height:24px;border:1.5px solid var(--white);border-radius:50%;display:flex;align-items:center;justify-content:center}

/* nav */
.nav{left:0;top:38px;width:1200px;height:75px;background:var(--white)}
.nav .brand{left:60px;top:24px;font-size:17px}
.nav-links{left:596px;top:28px;display:flex;gap:33px;font-size:14px;color:var(--blue)}
.nav .signup{left:1048px;top:19px;width:92px;height:36px}

/* hero */
.hero{left:0;top:113px;width:1200px;height:525px;background:linear-gradient(100deg,#9db8de 0%,#7fa2d4 45%,#6c93cb 100%)}
.hero h1{left:61px;top:140px;font-size:44px;line-height:52px;font-weight:600;color:var(--white)}
.hero p{left:61px;top:258px;width:460px;font-size:14px;line-height:22px;color:var(--white)}
.hero .btn{left:60px;top:342px;width:210px;height:38px}
.hero-arrow{top:246px;width:32px;height:32px;border:1.5px solid var(--white);border-radius:50%;display:flex;align-items:center;justify-content:center}
.badge{left:463px;top:499px;width:274px;height:274px;border-radius:50%;background:var(--white);border:10px solid var(--ring);display:flex;flex-direction:column;align-items:center;padding-top:62px}
.badge .brand{font-size:18px}
.pill{display:flex;align-items:center;gap:12px;border:3px solid var(--purple-soft);background:var(--purple);color:var(--white);border-radius:22px;height:38px;padding:0 14px 0 4px;font-size:14px;margin-top:12px}
.pill .ico{width:28px;height:28px;border-radius:50%;background:var(--white);display:flex;align-items:center;justify-content:center}

/* about */
.about-arc{left:-260px;top:690px;width:500px;height:420px;border-radius:50%;border:16px solid #f2f3f9}
.about-photo{left:70px;top:788px;width:354px;height:354px;border-radius:50%;border:12px solid var(--purple-soft);background:linear-gradient(135deg,#e8e4ea,#c7b6c4 55%,#8fb5d9)}
.about-line{left:424px;top:839px;width:90px;height:1px;background:#ddd}
.about-plus{left:514px;top:828px;width:24px;height:24px;border-radius:50%;background:var(--purple-soft);color:var(--purple);display:flex;align-items:center;justify-content:center;font-size:18px;line-height:1}
.about h2{left:503px;top:862px;font-size:27px;font-weight:600;color:var(--blue)}
.about .mission{left:503px;top:901px;font-size:13px;color:var(--blue)}
.about .body{left:503px;top:930px;width:570px;font-size:13px;line-height:22.5px}
.about .btn{left:501px;top:1069px;width:112px;height:36px}

/* services */
.services{left:0;top:1229px;width:1200px;height:582px;background:var(--tint)}
.services h2{left:0;top:48px;width:1200px;text-align:center;font-size:26px;font-weight:600;color:var(--blue)}
.svc-ring{left:433px;top:109px;width:334px;height:334px;border-radius:50%;border:1.5px solid #e2e2ec}
.svc-icon{width:74px;height:74px;border-radius:50%;background:var(--white);border:4px solid var(--ring);display:flex;align-items:center;justify-content:center}
.svc-label{font-size:17px;font-weight:500;color:var(--blue);line-height:26px}

/* promo band */
.promo-band{left:0;top:1812px;width:1200px;height:336px;background:var(--blue)}
.promo-band h2{left:61px;top:60px;font-size:27px;line-height:38px;font-weight:600;color:var(--white)}
.promo-band p{left:61px;top:146px;width:560px;font-size:13px;line-height:22px;color:var(--white)}
.promo-band .btn{left:61px;top:222px;width:209px;height:38px}
.promo-photo{left:752px;top:0;width:405px;height:336px;background:linear-gradient(160deg,#e7b9c5,#b44b8f 60%,#7d2f77)}
.promo-arc{left:1080px;top:-60px;width:260px;height:260px;border-radius:50%;border:10px solid #2a62b6}

/* reserve */
.reserve h2{left:0;top:2222px;width:1200px;text-align:center;font-size:28px;line-height:38px;font-weight:600;color:var(--blue)}
.reserve p{left:320px;top:2308px;width:560px;text-align:center;font-size:13px;line-height:22px}
.reserve .btn{left:499px;top:2386px;width:202px;height:36px}

/* process */
.process{left:0;top:2484px;width:1200px;height:497px;background:var(--tint-blue)}
.process h2{left:0;top:48px;width:1200px;text-align:center;font-size:28px;font-weight:600;color:var(--blue)}
.step{width:246px;height:246px;border-radius:50%;background:var(--white);border:4px solid var(--blue);border-top-color:#d9e0ef;border-right-color:#d9e0ef;display:flex;flex-direction:column;align-items:center;justify-content:center;text-align:center;padding:0 20px}
.step p{font-size:13.5px;line-height:22px;margin-top:14px}
.step-num{width:54px;height:54px;border-radius:50%;background:var(--white);border:3px solid var(--blue);color:var(--purple);font-size:22px;display:flex;align-items:center;justify-content:center}
.process .btn{left:521px;top:408px;width:158px;height:36px}

/* booking */
.booking{left:0;top:2981px;width:1200px;height:326px;background:var(--purple)}
.booking-photo{left:87px;top:0;width:376px;height:326px;background:linear-gradient(120deg,#f1ece9,#d9b8a0 55%,#8e5c7f)}
.field{background:var(--white);border-radius:2px;height:37px;padding:4px 10px}
.field small{display:block;font-size:10px;color:#888}
.field span{font-size:12px;color:#222}
.chev{position:absolute;right:12px;top:13px}
.booking .btn{left:507px;top:3148px;width:78px;height:34px;font-size:14px}
.cal{left:773px;top:44px;width:225px;height:225px;background:var(--white);border-radius:4px;padding:14px 16px}
.cal-head{display:flex;justify-content:space-between;color:var(--blue);font-size:13px;font-weight:600}
.cal-grid{display:grid;grid-template-columns:repeat(7,1fr);row-gap:12px;margin-top:10px;font-size:11px;text-align:center}
.cal-grid .dh{font-weight:600;color:#333}
.cal-grid .sel{background:var(--blue);color:var(--white);border-radius:50%;width:22px;height:22px;line-height:22px;margin:-5px auto 0}

/* footer */
.footer .brand{left:0;top:3380px;width:1200px;justify-content:center;font-size:18px}
.footer-links{left:0;top:3438px;width:1200px;display:flex;justify-content:center;gap:34px;font-size:14px;color:var(--blue);padding-left:0}
.f-ico{width:46px;height:46px;border-radius:50%;border:2px solid var(--purple);display:flex;align-items:center;justify-content:center}
.f-text{font-size:14px;color:var(--blue)}
.footer-rule{left:0;top:3591px;width:1200px;height:1px;background:#e7e7ee}
.social{left:0;top:3622px;width:1200px;display:flex;justify-content:center;gap:18px}
.social span{width:38px;height:38px;border-radius:50%;border:1.5px solid var(--blue);display:flex;align-items:center;justify-content:center}
.social span i{width:14px;height:14px;border-radius:50%;background:var(--blue)}
.social span:first-child{background:var(--blue)}
.social span:first-child i{background:var(--white)}
.bottombar{left:0;top:3684px;width:1200px;height:40px;background:var(--blue);color:var(--white);font-size:12px;text-align:center;line-height:40px}
</style>
</head>
<body>

<header>
  <div class="abs topbar">
    <div class="abs promo">Reserve your on-site mobile vaccine clinic today!</div>
    <div class="abs contact" style="left:596px">
      <span class="ico-circle"><svg width="12" height="12" viewBox="0 0 24 24" fill="#fff"><path d="M6.6 10.8a15 15 0 006.6 6.6l2.2-2.2c.3-.3.7-.4 1-.2 1.1.4 2.3.6 3.6.6.6 0 1 .4 1 1V20c0 .6-.4 1-1 1C10.6 21 3 13.4 3 4c0-.6.4-1 1-1h3.5c.6 0 1 .4 1 1 0 1.3.2 2.5.6 3.6.1.3 0 .7-.2 1z"/></svg></span>
      <span>Contact Us Today: <b>555-014-2273</b></span>
    </div>
    <div class="abs contact" style="left:893px">
      <span class="ico-circle"><svg width="12" height="10" viewBox="0 0 24 18" fill="none" stroke="#fff" stroke-width="2"><rect x="1" y="1" width="22" height="16"/><path d="M1 1l11 9 11-9"/></svg></span>
      <span>E-mail: hello@brightpathrovers.com</span>
    </div>
  </div>
  <nav class="abs nav">
    <div class="abs brand"><span class="brand-dot"></span>Brightpath Rovers</div>
    <div class="abs nav-links"><a href="#">Home</a><a href="#">About</a><a href="#">Services</a><a href="#">Schedule Today</a><a href="#">Pricing</a></div>
    <a class="btn btn-blue signup" href="#">Sign Up</a>
  </nav>
</header>

<section class="abs hero" role="img" aria-label="Photo of a nurse giving a vaccine injection to a smiling woman">
  <h1 class="abs">Making the workplace<br>a healthier place</h1>
  <p class="abs">Brightpath Rovers specializes in providing seamless, hassle-free, on-site mobile vaccine clinics.</p>
  <a class="btn btn-white" href="#">Schedule An Appoinment</a>
  <span class="abs hero-arrow" style="left:12px"><svg width="16" height="12" viewBox="0 0 16 12" fill="none" stroke="#fff" stroke-width="1.5"><path d="M15 6H1M6 1L1 6l5 5"/></svg></span>
  <span class="abs hero-arrow" style="left:1154px"><svg width="16" height="12" viewBox="0 0 16 12" fill="none" stroke="#fff" stroke-width="1.5"><path d="M1 6h14M10 1l5 5-5 5"/></svg></span>
</section>

<div class="abs badge">
  <div class="brand"><span class="brand-dot"></span>Brightpath Rovers</div>
  <div class="pill"><span class="ico"><svg width="14" height="14" viewBox="0 0 24 24" fill="#9c3f98"><path d="M6.6 10.8a15 15 0 006.6 6.6l2.2-2.2c.3-.3.7-.4 1-.2 1.1.4 2.3.6 3.6.6.6 0 1 .4 1 1V20c0 .6-.4 1-1 1C10.6 21 3 13.4 3 4c0-.6.4-1 1-1h3.5c.6 0 1 .4 1 1 0 1.3.2 2.5.6 3.6.1.3 0 .7-.2 1z"/></svg></span><b style="font-weight:600">555-014-2273</b></div>
  <div class="pill" style="font-size:12px;margin-top:8px"><span class="ico"><svg width="14" height="10" viewBox="0 0 24 18" fill="none" stroke="#9c3f98" stroke-width="2.5"><rect x="1" y="1" width="22" height="16"/><path d="M1 1l11 9 11-9"/></svg></span>hello@brightpathrovers.com</div>
</div>

<section class="about">
  <div class="abs about-arc"></div>
  <div class="abs about-photo" role="img" aria-label="Photo of a healthcare worker vaccinating a young woman"></div>
  <div class="abs about-line"></div>
  <div class="abs about-plus">+</div>
  <h2 class="abs">About <span class="accent">Brightpath Rovers</span></h2>
  <div class="abs mission">Brightpath Rovers, PLLC mission: Making the workplace a healthier place.</div>
  <p class="abs body">Brightpath Rovers, PLLC was started by local, Washington state licensed pharmacist with over 15 years experience vaccinating patients. She is a highly skilled immunizer and enjoys interacting with patients while providing this important preventative health services. Her vaccination experience spans from individual patient vaccinations to large clinics during community outbreaks.</p>
  <a class="btn btn-blue" href="#">Read More</a>
</section>

<section class="abs services">
  <h2 class="abs">Our <span class="accent">Services</span></h2>
  <div class="abs svc-ring"></div>
  <svg width="0" height="0" style="position:absolute"><defs><g id="syringe"><path d="M4 26l6-6" stroke="#1b4fa0" stroke-width="2"/><rect x="9" y="11" width="26" height="9" rx="1" transform="rotate(-30 22 15)" fill="#9c3f98"/><path d="M34 6l6-3" stroke="#1b4fa0" stroke-width="2"/></g></defs></svg>
  <div class="abs svc-icon" style="left:437px;top:119px"><svg width="44" height="30"><use href="#syringe"/></svg></div>
  <div class="abs svc-icon" style="left:676px;top:115px"><svg width="44" height="30"><use href="#syringe"/></svg></div>
  <div class="abs svc-icon" style="left:729px;top:256px"><svg width="44" height="30"><use href="#syringe"/></svg></div>
  <div class="abs svc-icon" style="left:398px;top:288px"><svg width="44" height="30"><use href="#syringe"/></svg></div>
  <div class="abs svc-icon" style="left:569px;top:400px"><svg width="44" height="30"><use href="#syringe"/></svg></div>
  <div class="abs svc-label" style="left:180px;top:131px;width:232px;text-align:right">Mobile vaccine clinics<br>providing Flu</div>
  <div class="abs svc-label" style="left:768px;top:128px">Pneumonia vaccines</div>
  <div class="abs svc-label" style="left:822px;top:281px">wellness screenings</div>
  <div class="abs svc-label" style="left:200px;top:313px;width:178px;text-align:right">Covid booster</div>
  <div class="abs svc-label" style="left:440px;top:482px;width:320px;text-align:center">Consulting Services For WA<br>Healthcare Entities</div>
</section>

<section class="abs promo-band" style="overflow:hidden">
  <div class="abs promo-arc"></div>
  <h2 class="abs">Flu And Covid 19 Vacccine Can Protect<br>You And Your Family.</h2>
  <p class="abs">Now Available At Selected Pharmacies. No crowded waiting rooms, no long lines, no hassle!</p>
  <a class="btn btn-white" href="#">Schedule An Appoinment</a>
  <div class="abs promo-photo" role="img" aria-label="Photo of two smiling women with bandages after vaccination, one holding a phone"></div>
</section>

<section class="reserve">
  <h2 class="abs">Reserve Your On-Site <span class="accent">Mobile Vaccine</span><br><span class="accent">Clinic Today!</span></h2>
  <p class="abs">Now Available At Selected Pharmacies. No crowded waiting rooms, no long lines, no hassle!</p>
  <a class="btn btn-blue" href="#">Scedule An Appoinment</a>
</section>

<section class="abs process">
  <h2 class="abs">Vaccination <span class="accent">Process</span></h2>
  <div class="abs step" style="left:120px;top:111px">
    <svg width="36" height="44" viewBox="0 0 36 44"><path d="M2 2h22l10 10v30H2z" fill="#9c3f98"/><path d="M18 32V18M12 24l6-6 6 6M11 35h14" stroke="#fff" stroke-width="2.5" fill="none"/></svg>
    <p>Submit Vaccine Clinic Needs Questionnaire.</p>
  </div>
  <div class="abs step" style="left:476px;top:111px">
    <svg width="48" height="44" viewBox="0 0 48 44"><rect x="2" y="6" width="34" height="32" fill="#9c3f98"/><path d="M10 2v8M28 2v8" stroke="#9c3f98" stroke-width="3"/><g fill="#fff"><rect x="7" y="16" width="6" height="5"/><rect x="16" y="16" width="6" height="5"/><rect x="7" y="25" width="6" height="5"/><rect x="16" y="25" width="6" height="5"/></g><circle cx="36" cy="32" r="10" fill="#1b4fa0" stroke="#fff" stroke-width="2"/><path d="M36 26v6h5" stroke="#fff" stroke-width="2" fill="none"/></svg>
    <p>Brightpath Rovers, PLLC will contact you to schedule on-site vaccine clinic.</p>
  </div>
  <div class="abs step" style="left:833px;top:111px">
    <svg width="36" height="48" viewBox="0 0 36 48"><rect x="2" y="24" width="14" height="20" fill="#9c3f98"/><rect x="5" y="18" width="8" height="6" fill="#9c3f98"/><rect x="20" y="14" width="12" height="30" fill="#9c3f98"/><path d="M26 2v12" stroke="#9c3f98" stroke-width="3"/></svg>
    <p>Prepare your employees for vaccine clinic day.</p>
  </div>
  <div class="abs step-num" style="left:310px;top:120px">1</div>
  <div class="abs step-num" style="left:666px;top:120px">2</div>
  <div class="abs step-num" style="left:1023px;top:120px">3</div>
  <svg class="abs" style="left:377px;top:216px" width="90" height="20" viewBox="0 0 90 20"><path d="M0 10h80" stroke="#1b4fa0" stroke-width="3"/><path d="M72 2l14 8-14 8z" fill="#1b4fa0"/></svg>
  <svg class="abs" style="left:733px;top:216px" width="90" height="20" viewBox="0 0 90 20"><path d="M0 10h80" stroke="#1b4fa0" stroke-width="3"/><path d="M72 2l14 8-14 8z" fill="#1b4fa0"/></svg>
  <a class="btn btn-blue" href="#">more information</a>
</section>

<section class="abs booking">
  <div class="abs booking-photo" role="img" aria-label="Photo of a doctor giving an injection to a smiling patient"></div>
  <div class="abs field" style="left:502px;top:57px;width:240px"><small>Select a Day</small><span>25.7.2022</span><svg class="chev" width="14" height="8"><path d="M1 1l6 6 6-6" stroke="#666" fill="none"/></svg></div>
  <div class="abs field" style="left:502px;top:111px;width:115px"><small>Start With</small><span>00.00 AM</span><svg class="chev" width="14" height="8"><path d="M1 1l6 6 6-6" stroke="#666" fill="none"/></svg></div>
  <div class="abs field" style="left:628px;top:111px;width:116px;padding-top:12px"><small>End With</small><svg class="chev" width="14" height="8"><path d="M1 1l6 6 6-6" stroke="#666" fill="none"/></svg></div>
  <div class="abs cal">
    <div class="cal-head"><span>Jun 2022</span><span style="color:#666;font-weight:400">&lsaquo;&nbsp;&nbsp;&rsaquo;</span></div>
    <div class="cal-grid">
      <span class="dh">M</span><span class="dh">T</span><span class="dh">W</span><span class="dh">T</span><span class="dh">F</span><span class="dh">S</span><span class="dh">S</span>
      <span>1</span><span>2</span><span>3</span><span>4</span><span>5</span><span>6</span><span>7</span>
      <span>8</span><span>9</span><span>10</span><span>11</span><span>12</span><span>13</span><span>14</span>
      <span>15</span><span>16</span><span>17</span><span>18</span><span>19</span><span>20</span><span>21</span>
      <span>22</span><span>23</span><span>24</span><span class="sel">25</span><span>26</span><span>27</span><span>28</span>
      <span>29</span><span>30</span>
    </div>
  </div>
</section>
<a class="btn btn-white booking-apply" href="#" style="left:507px;top:3148px;width:78px;height:34px">Apply</a>

<footer class="footer">
  <div class="abs brand"><span class="brand-dot"></span>Brightpath Rovers</div>
  <div class="abs footer-links"><a href="#">Home</a><a href="#">About</a><a href="#">Services</a><a href="#">Schedule Today</a><a href="#">Pricing</a></div>
  <div class="abs f-ico" style="left:473px;top:3486px"><svg width="18" height="18" viewBox="0 0 24 24" fill="#1b4fa0"><path d="M6.6 10.8a15 15 0 006.6 6.6l2.2-2.2c.3-.3.7-.4 1-.2 1.1.4 2.3.6 3.6.6.6 0 1 .4 1 1V20c0 .6-.4 1-1 1C10.6 21 3 13.4 3 4c0-.6.4-1 1-1h3.5c.6 0 1 .4 1 1 0 1.3.2 2.5.6 3.6.1.3 0 .7-.2 1z"/></svg></div>
  <div class="abs f-ico" style="left:658px;top:3486px"><svg width="20" height="15" viewBox="0 0 24 18" fill="none" stroke="#1b4fa0" stroke-width="2.5"><rect x="1" y="1" width="22" height="16"/><path d="M1 1l11 9 11-9"/></svg></div>
  <div class="abs f-text" style="left:420px;top:3544px;width:154px;text-align:center;font-weight:600">555-014-2273</div>
  <div class="abs f-text" style="left:575px;top:3544px;width:212px;text-align:center">hello@brightpathrovers.com</div>
  <div class="abs footer-rule"></div>
  <div class="abs social"><span><i></i></span><span><i></i></span><span><i></i></span><span><i></i></span></div>
  <div class="abs bottombar">2022© Brightpath Rovers PLLC. All right reserved.</div>
</footer>

</body>
</html>
```